10' Banner for Pest Control Company

I need a 10'x10' banner created for a Pest Control Company named, Brightfield Pest Control. It is a total service company so equal emphasis needs to be placed on bugs, termites, rodents, weeds, and tree services like Olive Tree spraying for fruit suppression. The main colors are Orange and Grey. This will be a banner for use at trade shows. It needs to show a customer at a glance exactly what we do and what our name is.
Our website is under development at http://dev.marlowbeck-example.com so you can visit there and get an idea of the colors used.
Thank you!
Updates

Project Deadline Extended
Reason: Deadline extended per some designer's requests.

Target Market(s)

People looking for pest control services in Phoenix, Arizona

Industry/Entity Type

Pest Control

Requirements
Must have
• Photos of pests.. bugs, rodents, termites, weeds, tree spraying
• Large logo
• Vibrant and eye catching

```html
<!DOCTYPE html>
<html lang="en">
<head>
<meta charset="utf-8">
<title>Brightfield Pest Control – Trade Show Banner</title>
<link rel="stylesheet" href="https://fonts.googleapis.com/css2?family=Roboto:wght@300;400;700&display=swap">
<style>
  :root {
    --orange: #f26a2a;
    --grey-dark: #3f3f41;
    --grey: #8a8b8d;
    --white: #ffffff;
    --ink: #1e1e1e;
  }
  * { margin: 0; padding: 0; box-sizing: border-box; }
  html, body { width: 1200px; height: 1200px; overflow: hidden; background: var(--white); }
  .banner {
    position: relative;
    width: 1200px; height: 1200px;
    background: var(--white);
    font-family: "Roboto", Arial, sans-serif;
    color: var(--grey-dark);
  }
  .headline {
    position: absolute; left: 0; right: 0; top: 40px;
    text-align: center;
  }
  .headline-main {
    display: block;
    font-weight: 300;
    font-size: 128px;
    line-height: 1;
    letter-spacing: 1px;
    color: var(--grey-dark);
  }
  .headline-sub {
    display: block;
    margin-top: 8px;
    font-weight: 700;
    font-size: 52px;
    line-height: 1.1;
    color: var(--grey-dark);
  }
  .headline-sub .accent { color: var(--orange); }
  .headline-shadow {
    position: absolute; left: 140px; right: 140px; top: 236px; height: 24px;
    background: radial-gradient(ellipse at 50% 0%, rgba(0,0,0,0.16), rgba(0,0,0,0) 70%);
  }
  .photo {
    position: absolute; width: 196px; height: 196px;
  }
  .photo-cockroach { left: 103px; top: 312px; background: linear-gradient(135deg, #7a2e12, #c9793f 55%, #e9d6c4); }
  .photo-rats      { left: 367px; top: 312px; background: linear-gradient(135deg, #d9d6d3, #5a524e 55%, #2e2a28); }
  .photo-termites  { left: 631px; top: 312px; background: linear-gradient(135deg, #e8e6e2, #e2b878 55%, #8a7058); }
  .photo-bee       { left: 894px; top: 312px; background: linear-gradient(135deg, #f0e020, #b08a40 55%, #b0602a); }
  .photo-ant       { left: 103px; top: 571px; background: linear-gradient(135deg, #a8c83a, #4f7a1c 60%, #2a2a22); }
  .photo-sprayer   { left: 367px; top: 571px; background: linear-gradient(135deg, #4e6e3a, #8fbf58 50%, #5b7a48); }

  .brand {
    position: absolute; left: 640px; top: 600px; width: 480px;
    display: flex; align-items: center; gap: 18px;
  }
  .brand-dot {
    flex: none; width: 26px; height: 26px; border-radius: 50%;
    background: var(--orange);
  }
  .brand-name {
    font-weight: 700;
    font-size: 50px;
    line-height: 1.05;
    color: var(--orange);
    text-transform: uppercase;
  }

  .tagline {
    position: absolute; left: 0; right: 0; top: 812px;
    text-align: center;
    font-weight: 400;
    font-size: 31px;
    letter-spacing: 0.5px;
    color: var(--orange);
  }

  .services {
    position: absolute; left: 0; right: 0; top: 874px; height: 199px;
    background: var(--orange);
  }
  .service-list {
    position: absolute; list-style: none;
  }
  .service-list.col-left  { left: 79px;  top: 36px; }
  .service-list.col-right { left: 556px; top: 40px; }
  .service-list li {
    display: flex; align-items: center; gap: 14px;
    height: 46.5px;
    font-size: 31px; font-weight: 400;
    color: var(--white);
  }
  .service-list svg { flex: none; width: 22px; height: 22px; }

  .contact {
    position: absolute; left: 79px; top: 1095px;
    color: var(--ink);
  }
  .contact-phone { font-size: 27px; font-weight: 400; }
  .contact-address { margin-top: 10px; font-size: 15px; }
  .website {
    position: absolute; right: 52px; top: 1110px;
    font-size: 27px; font-weight: 700;
    color: var(--orange);
  }
</style>
</head>
<body>
<main class="banner">
  <h1 class="headline">
    <span class="headline-main">HELPING YOU</span>
    <span class="headline-sub">GET RID OF ANNOYING <span class="accent">PESTS</span></span>
  </h1>
  <div class="headline-shadow"></div>

  <div class="photo photo-cockroach" role="img" aria-label="Close-up photo of a cockroach"></div>
  <div class="photo photo-rats" role="img" aria-label="Photo of two rats"></div>
  <div class="photo photo-termites" role="img" aria-label="Photo of termites on wood"></div>
  <div class="photo photo-bee" role="img" aria-label="Photo of a bee on a flower"></div>
  <div class="photo photo-ant" role="img" aria-label="Photo of an ant on a green leaf"></div>
  <div class="photo photo-sprayer" role="img" aria-label="Photo of a technician spraying trees with a backpack sprayer"></div>

  <div class="brand">
    <span class="brand-dot"></span>
    <span class="brand-name">Brightfield<br>Pest Control</span>
  </div>

  <p class="tagline">SAFE AND EFFECTIVE PEST CONTROL SOLUTIONS</p>

  <section class="services">
    <ul class="service-list col-left">
      <li><svg viewBox="0 0 22 22"><circle cx="11" cy="11" r="9.5" fill="none" stroke="#fff" stroke-width="2"/><path d="M9 7 L15 11 L9 15 Z" fill="#fff"/></svg>PEST CONTROL</li>
      <li><svg viewBox="0 0 22 22"><circle cx="11" cy="11" r="9.5" fill="none" stroke="#fff" stroke-width="2"/><path d="M9 7 L15 11 L9 15 Z" fill="#fff"/></svg>CUSTOM SPRAY SERVICES</li>
      <li><svg viewBox="0 0 22 22"><circle cx="11" cy="11" r="9.5" fill="none" stroke="#fff" stroke-width="2"/><path d="M9 7 L15 11 L9 15 Z" fill="#fff"/></svg>TERMITE CONTROL</li>
    </ul>
    <ul class="service-list col-right">
      <li><svg viewBox="0 0 22 22"><circle cx="11" cy="11" r="9.5" fill="none" stroke="#fff" stroke-width="2"/><path d="M9 7 L15 11 L9 15 Z" fill="#fff"/></svg>WEED CONTROL</li>
      <li><svg viewBox="0 0 22 22"><circle cx="11" cy="11" r="9.5" fill="none" stroke="#fff" stroke-width="2"/><path d="M9 7 L15 11 L9 15 Z" fill="#fff"/></svg>BEE HIVE REMOVAL</li>
      <li><svg viewBox="0 0 22 22"><circle cx="11" cy="11" r="9.5" fill="none" stroke="#fff" stroke-width="2"/><path d="M9 7 L15 11 L9 15 Z" fill="#fff"/></svg>PEST INSPECTION SERVICES</li>
    </ul>
  </section>

  <div class="contact">
    <p class="contact-phone">Call Now!!&nbsp; 602 555 0148</p>
    <p class="contact-address">1840 W. Canyon Ridge Road, Phoenix, AZ 85021</p>
  </div>
  <p class="website">www.dev.marlowbeck-example.com</p>
</main>
</body>
</html>
```